Brightpath7crew needs a website

We need a website so we can post future events of our company about business motivation. The site have to include a calendar on the "Home" page that when the user cliks on the day of the event , there should open a small page with the information of the event (location,time,subject of the event...) . We need also an "About Us" page with information about our company and what we do as well as "Contact" page with our email and phone number and access to our facebook page. We would like to have a private access for users ("Restricted access") but they have to put their e-mail and password to access the special page (log in). On the 'special page' we would like to have some videos and photos that we will post on that page regularly .
Here is a website that would be an exemple of how we would like to have ours
http://summitlarkacademy.example
The needs to be responsed and with backoffice

Industry/Entity Type

Business

Number of Pages Required

3 page

Colors
9bcb3c
f37122

Requirements
Must have
• Must have a restricted access page so the user can place a user name and a secret password.

```html
<!DOCTYPE html>
<html lang="en">
<head>
<meta charset="utf-8">
<title>Brightpath7crew — Making Ideas Happen</title>
<link href="https://fonts.googleapis.com/css2?family=Open+Sans:wght@400;600;700&family=Oswald:wght@300;400&family=Arimo:wght@400;700&display=swap" rel="stylesheet">
<style>
:root{
  --green:#9bcb3c;
  --orange:#f37122;
  --ink:#333333;
  --muted:#555555;
  --panel:#e8e8e8;
  --panel-line:#d2d2d2;
  --footer:#3d3d3d;
  --footer-deep:#2b2b2b;
  --white:#ffffff;
}
*{box-sizing:border-box;margin:0;padding:0}
html,body{width:1200px;height:2965px;overflow:hidden}
body{position:relative;font-family:"Open Sans",Arial,sans-serif;color:var(--ink);
  background:linear-gradient(#d6d6d6 800px,#f2f2f2 1300px,#ffffff 2000px)}
.abs{position:absolute}

/* hero */
.hero-photo{left:0;top:0;width:1200px;height:800px;
  background:radial-gradient(ellipse at 60% 35%,#8b7d72 0%,#4e4640 45%,#262220 100%)}
.header-band{left:0;top:0;width:1200px;height:138px;background:rgba(20,20,20,.72);border-bottom:1px solid rgba(255,255,255,.25)}
.brand{left:90px;top:40px;color:var(--white);font-family:"Arimo",Arial,sans-serif;font-weight:700;font-size:27px;display:flex;align-items:center;gap:12px}
.brand-square{width:22px;height:22px;background:var(--green)}
.nav{left:355px;top:90px;display:flex;gap:0}
.nav a{color:var(--white);text-decoration:none;font-size:16px;position:relative;padding-bottom:22px}
.nav a.active{color:var(--orange)}
.nav a.active::after{content:"";position:absolute;left:0;right:0;bottom:0;height:3px;background:var(--orange)}
.account{left:975px;top:88px;font-size:16px;color:var(--white)}
.account .login{color:var(--green)}
.account .register{color:var(--orange)}
.hero-title{left:0;width:1200px;text-align:center;color:var(--white)}
.hero-title .line1{font-size:56px;font-weight:400;top:232px;position:absolute;width:100%}
.hero-title .line2{font-size:56px;font-weight:700;top:300px;position:absolute;width:100%}
.next-event{left:818px;top:502px;color:var(--white)}
.next-event h3{font-size:28px;font-weight:400}
.next-event p{font-size:22px;margin-top:10px}
.btn{display:inline-flex;align-items:center;justify-content:center;background:var(--orange);color:var(--white);
  border-radius:30px;font-weight:400;box-shadow:0 2px 4px rgba(0,0,0,.3)}
.hero-btn{left:820px;top:632px;width:262px;height:58px;font-size:21px}

/* info panel */
.panel{left:150px;top:760px;width:915px;height:530px;background:var(--panel);box-shadow:0 0 6px rgba(0,0,0,.15)}
.subscribe{left:165px;top:804px;display:flex;align-items:center;gap:10px;font-size:10.5px;text-transform:uppercase}
.subscribe .field{width:115px;height:22px;background:#f5f5f5;border:1px solid #cfcfcf;font-size:10px;color:#888;padding:4px 6px;text-transform:none}
.subscribe .field.wide{width:165px}
.subscribe .send{width:76px;height:20px;background:var(--orange);color:var(--white);font-size:10px;text-align:center;line-height:20px}
.divider-h{left:165px;top:846px;width:600px;height:1px;background:var(--panel-line)}
.divider-v{top:846px;width:1px;height:420px;background:var(--panel-line)}
.col-title{font-family:"Oswald",sans-serif;font-weight:300;font-size:34px;color:var(--ink);letter-spacing:-1px}
.col-title span{color:var(--green)}
.col-text{font-size:13.5px;line-height:21px;color:var(--ink)}
.read-more{font-size:13.5px;color:var(--orange)}
.events-side{left:765px;top:760px;width:300px;height:530px;background:#f1f1f1}
.events-side .col-title{position:absolute;left:23px;top:22px}
.see-all{position:absolute;left:208px;top:50px;font-size:12px;color:var(--green)}
.event-row{position:absolute;left:15px;width:270px;display:flex;gap:10px;border-bottom:1px solid var(--panel-line);padding-bottom:6px}
.event-date{width:36px;height:42px;background:var(--green);color:var(--white);font-size:13px;line-height:14px;text-align:center;padding-top:6px;flex:none}
.event-date small{font-size:9px;display:block}
.event-date.past{background:#6a6a5a}
.event-row p{font-size:11px;line-height:12px;color:var(--ink)}
.login-tip{left:878px;top:960px;width:262px;height:56px;background:var(--orange);color:var(--white);border-radius:28px;
  font-size:14px;text-align:center;line-height:19px;padding-top:9px;box-shadow:0 2px 4px rgba(0,0,0,.25)}

/* calendar */
.cal-title{left:0;width:1200px;top:1368px;text-align:center;font-family:"Oswald",sans-serif;font-weight:300;font-size:34px;letter-spacing:-1px}
.cal-title span{color:var(--green)}
.calendar{left:152px;top:1435px;width:898px;height:900px;display:grid;grid-template-columns:repeat(4,1fr);grid-template-rows:repeat(4,1fr);
  border-radius:10px;overflow:hidden;gap:1px;background:#e6e6e6}
.day{position:relative;background:linear-gradient(160deg,#3a4f93 0%,#1e2454 55%,#130f24 100%);color:var(--white);
  text-align:center;font-size:58px;line-height:62px;padding-top:20px}
.day:nth-child(4n+2){background:linear-gradient(160deg,#4f5f9e,#232c63 60%,#1a1530)}
.day:nth-child(4n+3){background:linear-gradient(160deg,#3d3050,#1f2446 60%,#1a1020)}
.day:nth-child(4n){background:linear-gradient(160deg,#6a5a55,#2b2a4a 60%,#161326)}
.day .yr{font-size:44px}
.event-pop{left:607px;top:1603px;width:303px;height:530px;background:var(--white);border-radius:0 0 12px 12px;box-shadow:0 3px 10px rgba(0,0,0,.35);text-align:center}
.pop-head{position:absolute;left:0;top:0;width:303px;height:100px}
.pop-head-text{position:absolute;left:0;top:8px;width:100%;color:var(--white);font-size:27px;line-height:34px}
.pop-body{position:absolute;left:30px;top:135px;width:243px;font-size:15.5px;line-height:21px;color:var(--ink)}
.pop-body h4{font-weight:400;font-size:19px;margin-bottom:20px}
.pop-body p{margin-bottom:20px}
.pop-btn{left:38px;top:458px;width:228px;height:42px;font-size:18px;position:absolute}

/* footer */
.footer{left:0;top:2470px;width:1200px;height:390px;background:var(--footer);color:var(--white);font-family:"Arimo",Arial,sans-serif}
.footer h5{position:absolute;top:86px;font-size:19px;font-weight:700}
.foot-links{position:absolute;left:64px;top:154px;list-style:none;font-size:16px;line-height:35px}
.touch{position:absolute;left:237px;top:152px;width:205px;font-size:14px;line-height:17px}
.touch .rule{border-top:1px dotted #bbb;margin:0 0 30px}
.seat-form{position:absolute;left:483px;top:158px;width:287px}
.seat-form .field{height:34px;background:#f0f0f0;border-radius:5px;margin-bottom:8px;color:#555;font-size:13px;padding:9px 15px}
.seat-form .submit{height:32px;background:var(--orange);border-radius:5px;text-align:center;font-size:13px;line-height:32px}
.gallery{position:absolute;left:800px;top:162px;display:grid;grid-template-columns:repeat(4,76px);gap:14px 15px}
.gallery div{height:76px;background:linear-gradient(150deg,#8a4a3a,#2f2b5a 60%,#151020)}
.gallery div:nth-child(4n){background:linear-gradient(150deg,#3c5f8f,#1b2440)}
.copyright{left:0;top:2860px;width:1200px;height:105px;background:var(--footer-deep);color:var(--white);font-family:"Arimo",Arial,sans-serif;font-size:15px;padding:43px 0 0 98px}
</style>
</head>
<body>

<div class="abs hero-photo" role="img" aria-label="Close-up of a stage microphone in a blurred conference hall"></div>
<div class="abs header-band"></div>
<div class="abs brand"><span>Brightpath7crew</span><span class="brand-square"></span></div>
<nav class="abs nav">
  <a class="active" href="#" style="margin-right:63px">HOME</a>
  <a href="#" style="margin-right:78px">ABOUT US</a>
  <a href="#" style="margin-right:72px">CALENDAR</a>
  <a href="#">CONTACT</a>
</nav>
<div class="abs account"><span class="login">Log in</span> or <span class="register">Register</span></div>

<div class="abs hero-title">
  <div class="line1">IT’S ABOUT</div>
  <div class="line2">MAKING IDEAS HAPPEN</div>
</div>
<div class="abs next-event">
  <h3>NEXT TRAINING EVENT</h3>
  <p>LISBOA, 5. June 2016.</p>
</div>
<div class="abs btn hero-btn">GET YOUR SEAT!</div>

<section class="abs panel"></section>
<div class="abs subscribe">
  <span>Subscribe to our email news</span>
  <span class="field">Name</span>
  <span class="field wide">Email</span>
  <span class="send">SUBMIT</span>
</div>
<div class="abs divider-h"></div>
<div class="abs divider-v" style="left:382px"></div>
<div class="abs divider-v" style="left:765px;top:760px;height:530px"></div>

<div class="abs" style="left:200px;top:872px;width:170px">
  <h2 class="col-title">WHO WE <span>ARE</span></h2>
  <p class="col-text" style="margin-top:16px">Brightpath7crew is an organization that brings together thousands of entrepreneurs worldwide whose sole mission is to impact the lives of others.</p>
  <p class="read-more" style="margin-top:20px">Read more...</p>
</div>
<div class="abs" style="left:415px;top:858px;width:345px">
  <h2 class="col-title">WHAT WE <span>DO</span></h2>
  <p class="col-text" style="margin-top:16px">Our mission is to Impact the lives of millions of people around the world by helping them through our incredible proven system, with hard work and dedication</p>
  <p class="read-more" style="margin-top:18px">Read more...</p>
  <h2 class="col-title" style="margin-top:30px">WHY <span>US?</span></h2>
  <p class="col-text" style="margin-top:16px">We are a group of passionate entrepreneurs who value the people we do business with. Many people have seen their lives impacted by joining us.</p>
  <p class="read-more" style="margin-top:18px">Read more...</p>
</div>

<aside class="abs events-side">
  <h2 class="col-title">LATEST <span>EVENTS</span></h2>
  <span class="see-all">SEE ALL</span>
  <div class="event-row" style="top:118px"><div class="event-date">2<small>Mar</small></div><p>Lorem ipsum dolor sit amet, consectetur adipiscing elit, sed do eiusmod tempor incididunt ut labore et dolore magna aliqua.</p></div>
  <div class="event-row" style="top:187px"><div class="event-date past">2<small>Mar</small></div><p>Lorem ipsum dolor sit amet, consectetur adipiscing elit, sed do eiusmod tempor incididunt ut labore et dolore magna aliqua.</p></div>
  <div class="event-row" style="top:256px"><div class="event-date">2<small>Mar</small></div><p>Lorem ipsum dolor sit amet, consectetur adipiscing elit, sed do eiusmod tempor incididunt ut labore et dolore magna aliqua.</p></div>
  <div class="event-row" style="top:325px"><div class="event-date">2<small>Mar</small></div><p>Lorem ipsum dolor sit amet, consectetur adipiscing elit, sed do eiusmod tempor incididunt ut labore et dolore magna aliqua.</p></div>
  <div class="event-row" style="top:394px"><div class="event-date">2<small>Mar</small></div><p>Lorem ipsum dolor sit amet, consectetur adipiscing elit, sed do eiusmod tempor incididunt ut labore et dolore magna aliqua.</p></div>
  <div class="event-row" style="top:463px"><div class="event-date">2<small>Mar</small></div><p>Lorem ipsum dolor sit amet, consectetur adipiscing elit, sed do eiusmod tempor incididunt ut labore et dolore magna aliqua.</p></div>
</aside>
<div class="abs login-tip">You must be loged in!<br>Please, register or log in!</div>

<h2 class="abs cal-title">EVENTS <span>CALENDAR</span></h2>
<div class="abs calendar">
  <div class="day" role="img" aria-label="Conference audience photo">23.<br>May<br><span class="yr">2016.</span></div>
  <div class="day" role="img" aria-label="Conference audience photo">24.<br>May<br><span class="yr">2016.</span></div>
  <div class="day" role="img" aria-label="Conference audience photo">30.<br>May<br><span class="yr">2016.</span></div>
  <div class="day" role="img" aria-label="Conference audience photo">05.<br>June<br><span class="yr">2016.</span></div>
  <div class="day" role="img" aria-label="Conference audience photo">23.<br>May<br><span class="yr">2016.</span></div>
  <div class="day" role="img" aria-label="Conference audience photo">24.<br>May<br><span class="yr">2016.</span></div>
  <div class="day" role="img" aria-label="Conference audience photo">30.<br>May<br><span class="yr">2016.</span></div>
  <div class="day" role="img" aria-label="Conference audience photo">05.<br>June<br><span class="yr">2016.</span></div>
  <div class="day" role="img" aria-label="Conference stage photo">23.<br>May<br><span class="yr">2016.</span></div>
  <div class="day" role="img" aria-label="Conference stage photo">24.<br>May<br><span class="yr">2016.</span></div>
  <div class="day" role="img" aria-label="Conference stage photo">30.<br>May<br><span class="yr">2016.</span></div>
  <div class="day" role="img" aria-label="Conference stage photo">05.<br>June<br><span class="yr">2016.</span></div>
  <div class="day" role="img" aria-label="Speaker on stage photo">23.<br>May<br><span class="yr">2016.</span></div>
  <div class="day" role="img" aria-label="Speaker on stage photo">24.<br>May<br><span class="yr">2016.</span></div>
  <div class="day" role="img" aria-label="Speaker on stage photo">30.<br>May<br><span class="yr">2016.</span></div>
  <div class="day" role="img" aria-label="Speaker on stage photo">05.<br>June<br><span class="yr">2016.</span></div>
</div>

<div class="abs event-pop">
  <svg class="pop-head" viewBox="0 0 303 100" width="303" height="100"><polygon points="0,0 303,0 303,78 151.5,100 0,78" fill="#f37122"/></svg>
  <div class="pop-head-text">24. May 2016.<br>Lisboa</div>
  <div class="pop-body">
    <h4>LOREM IPSUM</h4>
    <p>Lorem ipsum dolor sit amet, consectetur adipiscing elit, sed do eiusmod tempor incididunt ut labore et dolore magna aliqua.</p>
    <p>Lorem ipsum dolor sit amet, consectetur adipiscing elit, sed do eiusmod tempor incididunt ut labore et dolore magna aliqua.</p>
  </div>
  <div class="btn pop-btn">GET YOUR SEAT!</div>
</div>

<footer class="abs footer">
  <h5 style="left:64px">Quick links</h5>
  <h5 style="left:240px">Get In Touch</h5>
  <h5 style="left:487px">Get Your Seat</h5>
  <h5 style="left:803px">Photo Wall</h5>
  <ul class="foot-links"><li>HOME</li><li>ABOUT US</li><li>CALENDAR</li><li>CONTACT</li></ul>
  <div class="touch">
    <div class="rule"></div>
    <p>Phone Us<br>+408-555-0142</p>
    <div class="rule" style="margin:16px 0 26px"></div>
    <p>Email Us<br>contact@brightpath7crew.example</p>
  </div>
  <div class="seat-form">
    <div class="field">Your name</div>
    <div class="field">Your email address</div>
    <div class="field">Your phone number</div>
    <div class="submit">Submit</div>
  </div>
  <div class="gallery">
    <div role="img" aria-label="Event photo"></div><div role="img" aria-label="Event photo"></div><div role="img" aria-label="Event photo"></div><div role="img" aria-label="Speaker photo"></div>
    <div role="img" aria-label="Event photo"></div><div role="img" aria-label="Event photo"></div><div role="img" aria-label="Event photo"></div><div role="img" aria-label="Speaker photo"></div>
  </div>
</footer>
<div class="abs copyright">© 2016 Brightpath7crew, All Right Reserved.</div>

</body>
</html>
```